Bright Loom Allies, LLC
Collaborative Contract Solutions
Modern
Owen Darby
Managing Director
12 Juniper Vale Road
Suite 240
Pelham Ridge, NH 01847
owen@brightloomallies.com
www.brightloomallies.com
Docs said to upload this logo format.

```html
<!DOCTYPE html>
<html lang="en">
<head>
<meta charset="utf-8">
<title>Bright Loom Allies, LLC — Business Cards</title>
<link href="https://fonts.googleapis.com/css2?family=Source+Sans+3:ital,wght@0,400;0,600;0,700;1,700&display=swap" rel="stylesheet">
<style>
  :root{
    --stage:#e9ebee;
    --card:#ffffff;
    --brand:#1d5fae;
    --band-light:#3a8ad6;
    --band-dark:#145299;
    --band-rule:#cfe1f4;
    --ink:#3c3f44;
    --white:#ffffff;
  }
  *{box-sizing:border-box;margin:0;padding:0}
  html,body{width:1200px;height:852px;overflow:hidden}
  body{background:var(--stage);font-family:"Source Sans 3",Arial,sans-serif;color:var(--ink);position:relative}

  .card{position:absolute;width:560px;height:320px;background:var(--card);border-radius:18px;overflow:hidden;box-shadow:0 6px 18px rgba(0,0,0,.12)}
  .card--front{left:30px;top:110px}
  .card--back{left:610px;top:420px}

  .brand{position:absolute;left:0;right:0;display:flex;align-items:center;justify-content:center;gap:10px}
  .brand__dot{width:16px;height:16px;border-radius:50%;background:var(--brand)}
  .brand__name{font-weight:700;font-size:30px;color:var(--brand);letter-spacing:-.3px;white-space:nowrap}
  .card--front .brand{top:52px}
  .card--back .brand{top:60px}

  .band{position:absolute;left:0;right:0;background:linear-gradient(180deg,var(--band-light),var(--band-dark));color:var(--white)}
  .card--front .band{top:122px;height:46px;display:flex;align-items:center;justify-content:center;gap:28px;border-top:3px solid var(--band-rule);border-bottom:3px solid var(--band-rule)}
  .band__name{font-weight:700;font-style:italic;font-size:20px}
  .band__sep{font-size:20px;font-weight:600}
  .band__title{font-weight:600;font-style:italic;font-size:15px}

  .front-details{position:absolute;left:0;right:0;top:196px;text-align:center;font-size:14px;line-height:22px;white-space:nowrap}
  .front-details .label{color:var(--brand);font-weight:700}
  .front-details .row span{margin:0 4px}

  .card--back .band{top:176px;bottom:0;border-top:3px solid var(--band-rule);display:flex}
  .person{width:280px;padding:24px 20px 0 0;text-align:center}
  .person__name{font-weight:700;font-style:italic;font-size:20px;line-height:24px}
  .person__title{font-weight:600;font-style:italic;font-size:15px;line-height:20px}
  .person__addr{margin-top:14px;font-size:13px;line-height:18px}
  .divider{width:1px;background:rgba(255,255,255,.55);margin:22px 0 26px}
  .contacts{list-style:none;padding:20px 0 0 16px;font-size:13px;line-height:26px}
  .contacts li{display:flex;align-items:center;gap:8px;white-space:nowrap}
  .contacts svg{width:15px;height:15px;flex:none}
</style>
</head>
<body>

<section class="card card--front" aria-label="Business card front">
  <div class="brand"><span class="brand__dot"></span><span class="brand__name">Bright Loom Allies</span></div>
  <div class="band">
    <span class="band__name">Owen Darby</span>
    <span class="band__sep">/</span>
    <span class="band__title">Managing Director</span>
  </div>
  <div class="front-details">
    <p>12 Juniper Vale Road, Suite 240, Pelham Ridge, NH 01847</p>
    <p class="row"><span><b class="label">P:</b> 978.410.2276</span><span><b class="label">C:</b> 978.655.3018</span><span><b class="label">E:</b> owen@brightloomallies.com</span></p>
    <p><b class="label">W:</b> www.brightloomallies.com</p>
  </div>
</section>

<section class="card card--back" aria-label="Business card back">
  <div class="brand"><span class="brand__dot"></span><span class="brand__name">Bright Loom Allies</span></div>
  <div class="band">
    <div class="person">
      <p class="person__name">Owen Darby</p>
      <p class="person__title">Managing Director</p>
      <p class="person__addr">12 Juniper Vale Road<br>Suite 240, Pelham Ridge, NH 01847</p>
    </div>
    <div class="divider"></div>
    <ul class="contacts">
      <li><svg viewBox="0 0 16 16" aria-hidden="true"><path fill="#fff" d="M4 1.5l2 3-1.3 1.3a8 8 0 0 0 5.5 5.5L11.5 10l3 2-1 2.5C8 14.5 1.5 8 1.5 2.5z"/></svg>978.410.2276</li>
      <li><svg viewBox="0 0 16 16" aria-hidden="true"><rect x="4.5" y="1" width="7" height="14" rx="1.5" fill="#fff"/><rect x="6" y="3" width="4" height="8" fill="#2a75c4"/></svg>978.655.3018</li>
      <li><svg viewBox="0 0 16 16" aria-hidden="true"><rect x="1" y="3.5" width="14" height="9" rx="1" fill="#fff"/><path d="M1.5 4l6.5 5 6.5-5" fill="none" stroke="#2a75c4" stroke-width="1.2"/></svg>owen@brightloomallies.com</li>
      <li><svg viewBox="0 0 16 16" aria-hidden="true"><circle cx="8" cy="8" r="6.5" fill="none" stroke="#fff" stroke-width="1.4"/><path d="M1.5 8h13M8 1.5c-3 3.5-3 9.5 0 13M8 1.5c3 3.5 3 9.5 0 13" fill="none" stroke="#fff" stroke-width="1.1"/></svg>www.brightloomallies.com</li>
    </ul>
  </div>
</section>

</body>
</html>
```